Please design a business card with my current logo (attached below).

I have some specifics that must be included:
1. I want the emphasis on Accredited Legacy Home Transfer Advisor.
2. Leave room for my picture.
3. Company name, address, phone numbers and email address.
4. My BRE# should be placed under my name.

```html
<!DOCTYPE html>
<html lang="en">
<head>
<meta charset="utf-8">
<title>Nora Whitfield – Business Card</title>
<link rel="stylesheet" href="https://fonts.googleapis.com/css2?family=Cinzel:wght@600;700&family=Crimson+Text&family=Source+Sans+3:wght@400&display=swap">
<style>
  :root {
    --ink: #363435;
    --crimson: #a52433;
    --paper: #ffffff;
    --frame: #2b2a2a;
  }
  * { margin: 0; padding: 0; box-sizing: border-box; }
  html, body { width: 1200px; height: 1000px; overflow: hidden; background: var(--paper); }
  .sheet { position: relative; width: 1200px; height: 1000px; }

  .side-label {
    position: absolute; left: 164px;
    font-family: "Crimson Text", serif; font-size: 31px; color: #222;
  }
  .side-label--front { top: 266px; }
  .side-label--back { top: 707px; }

  .card {
    position: absolute; left: 313px; width: 745px; height: 427px;
    border: 2px solid var(--frame); background: var(--paper); overflow: hidden;
  }
  .card--front { top: 59px; }
  .card--back { top: 499px; }
  .card svg.shapes { position: absolute; left: 0; top: 0; }

  .brand-mark { position: absolute; background: var(--crimson); }
  .card--front .brand-mark { left: 336px; top: 60px; width: 70px; height: 70px; }
  .card--back .brand-mark { left: 158px; top: 118px; width: 52px; height: 52px; }

  .agent-name {
    position: absolute; font-family: "Cinzel", serif; font-weight: 600;
    color: var(--ink); text-align: center; white-space: nowrap; line-height: 1;
  }
  .card--front .agent-name { left: 0; width: 741px; top: 194px; font-size: 68px; }
  .card--back .agent-name { left: 20px; width: 330px; top: 222px; font-size: 36px; }

  .designation {
    position: absolute; font-family: "Cinzel", serif; font-weight: 700;
    text-align: center; white-space: nowrap;
  }
  .card--front .designation {
    left: 0; width: 741px; top: 316px; font-size: 44px; line-height: 44px; color: var(--paper);
  }
  .card--back .designation {
    left: 20px; width: 330px; top: 268px; font-size: 24px; line-height: 28px; color: var(--crimson);
  }

  .contact {
    position: absolute; left: 435px; top: 20px;
    font-family: "Source Sans 3", sans-serif; font-size: 27px; line-height: 32.5px; color: var(--paper);
  }
  .photo-slot {
    position: absolute; left: 435px; top: 188px; width: 137px; height: 149px;
    background: var(--paper); color: var(--ink);
    font-family: "Source Sans 3", sans-serif; font-size: 26px; line-height: 36px;
    display: flex; align-items: center; justify-content: center; text-align: center;
  }
  .agent-id {
    position: absolute; left: 435px; top: 346px;
    font-family: "Source Sans 3", sans-serif; font-size: 27px; line-height: 31px; color: var(--paper);
  }
</style>
</head>
<body>
<main class="sheet">
  <p class="side-label side-label--front">front</p>
  <p class="side-label side-label--back">back</p>

  <section class="card card--front" aria-label="Card front">
    <svg class="shapes" width="741" height="423" viewBox="0 0 741 423">
      <rect x="0" y="276" width="741" height="147" fill="var(--ink)"/>
      <rect x="0" y="276" width="741" height="20" fill="var(--crimson)"/>
      <polygon points="0,270 741,270 741,276 372,296 0,276" fill="var(--paper)"/>
    </svg>
    <div class="brand-mark"></div>
    <h1 class="agent-name">Nora Whitfield</h1>
    <p class="designation">Accredited Legacy<br>Home Transfer Advisor</p>
  </section>

  <section class="card card--back" aria-label="Card back">
    <svg class="shapes" width="741" height="423" viewBox="0 0 741 423">
      <path d="M355,0 C312,78 317,178 357,278 C377,328 387,378 391,423 L741,423 L741,0 Z" fill="var(--crimson)"/>
      <path d="M370,0 C337,78 342,178 377,278 C392,328 395,378 397,423 L741,423 L741,0 Z" fill="var(--ink)"/>
    </svg>
    <div class="brand-mark"></div>
    <h2 class="agent-name">Nora Whitfield</h2>
    <p class="designation">Accredited Legacy<br>Home Transfer Advisor</p>
    <address class="contact">
      Company Name<br>
      Adress<br>
      #123 - 4567<br>
      #890- 1234<br>
      email@email.com
    </address>
    <div class="photo-slot">photo<br>here</div>
    <p class="agent-id">Your Name<br>BRE#</p>
  </section>
</main>
</body>
</html>
```